Bold and Elegant Tri-Fold Togo Menu

We are working on a togo menu which will be hand our to our customer. It will be printed on a 11x17 tri-fold paper. So there will be 2 pages and 4 columns. I have a layout in my mine, but you can change it if you have better idea. My restaurant is called Lantern Jade Chinese Bistro. I will like the theme color in Red which color to burgundy, with black and white.

***Please Ignore Special Requirements or Template. They have the wrong size listed.

I have some photo shot, however it is too big to upload here. You can download it at https://files.example.net/folders/7Kq2Xm9PzLw4RtYv8NbHc3JdE5s?share=1

Target Market(s)

We are target 30-60 middle class and retires.

Font styles to use
Other font styles liked:
• Title - Script, content - easy to read is fine

Colors
ec1f27
ffffff
000000
757575

Requirements
Must have
• A bold eyes catching front page. In the menu text should be easy to read but still elegant.
• Front page should contain the following info.
• LOGO
• Casual Chinese Restaurant
• Carry Out Menu
• Address: 2871 W Orchard Ave, St Charles IL 60178
• Phone: 630-412-8836
• Web Address: www.LanternJade.example
• Hours: Tuesday-Thursday 11:00am - 9:00pm
• Friday - Saturday 11:00am - 9:30pm
• Sun 12:00noon - 9:00pm
• Closed On Monday
• Dine In - Carry Out - Delivery - Catering
• B.Y.O.B. Welcome
• Simple Sketch Mini Map at the back cover. I can provide one if you need.
Nice to have
• We will provide some photo to place on the menu. Some touch-up will be nice.
• Proof read and correct our restaurant description will be a plus.
Should not have
• Too casual or comical fonts and graphic.

```html
<!DOCTYPE html>
<html lang="en">
<head>
<meta charset="utf-8">
<title>Lantern Jade Chinese Bistro – Carry Out Menu</title>
<link rel="stylesheet" href="https://fonts.googleapis.com/css2?family=Lobster&family=Open+Sans:ital,wght@0,400;0,600;0,700;1,600;1,700&family=Roboto+Condensed:ital,wght@0,400;0,700;1,700&display=swap">
<style>
:root{
  --burgundy:#7c1c24;
  --burgundy-deep:#5e1218;
  --red:#ec1f27;
  --black:#000;
  --white:#fff;
  --grey:#757575;
  --ink:#f6e6e6;
}
*{margin:0;padding:0;box-sizing:border-box}
html,body{width:1200px;height:776px;overflow:hidden;background:var(--burgundy)}
.sheet{position:relative;width:1224px;height:792px;transform:scale(.98039);transform-origin:0 0;
  background:var(--burgundy);color:var(--ink);font-family:"Open Sans",Arial,sans-serif;font-size:7px}
.block{position:absolute}
.row{display:flex;justify-content:space-between;align-items:baseline}
.item{font-weight:700;color:var(--white);font-size:7.2px}
.note{font-size:5px;color:var(--ink);opacity:.9;margin-top:1px}
.price{color:var(--white);font-size:7.4px}
.script-title{font-family:"Lobster",cursive;font-size:19px;color:var(--white);display:flex;align-items:center;gap:8px;white-space:nowrap}
.script-title::before,.script-title::after{content:"";flex:1;height:1px;background:var(--white)}
.script-title.left::before{flex:0 0 0}
.section-head{font-family:"Open Sans",sans-serif;font-style:italic;font-weight:700;font-size:13px;color:var(--white)}
.bullets{list-style:none;font-size:6.8px;color:var(--white);line-height:12.6px}
.bullets li::before{content:"• "}
.opt{display:grid;font-size:7px;color:var(--white);white-space:nowrap}
.photo{position:absolute;border:2px solid var(--white)}
.legend{position:absolute;left:0;top:702px;width:612px;height:90px;background:var(--black);padding:10px 22px;font-size:7px;color:var(--white)}
.legend .key{display:flex;align-items:center;gap:8px;font-weight:600}
.legend .dot{width:17px;height:17px;border-radius:50%;display:inline-block}
.pill{position:absolute;left:626px;top:48px;width:278px;height:48px;border-radius:24px;background:var(--white);
  color:var(--red);font-weight:700;font-size:14px;text-align:center;line-height:17px;padding-top:6px}
.notice{position:absolute;left:612px;top:397px;width:306px;height:40px;background:var(--black);color:var(--white);
  font-size:9.6px;padding:5px 14px 0 14px;display:flex;gap:6px;line-height:14px}
.notice b{font-style:italic}
.front-photos{position:absolute;left:918px;top:110px;width:306px;height:325px;background:var(--red);
  display:grid;grid-template-columns:192px 1fr;grid-template-rows:110px 110px 1fr;gap:5px;padding:5px 0}
.front-photos span{display:block}
.brand{position:absolute;left:948px;top:32px;display:flex;align-items:center;gap:10px}
.brand .name{font-family:"Open Sans",sans-serif;font-weight:700;font-size:27px;color:var(--red);line-height:28px}
.brand .mark{width:36px;height:36px;background:var(--red)}
.front-text{position:absolute;left:918px;width:306px;text-align:center;font-family:"Roboto Condensed",sans-serif}
.tagline{top:444px;color:var(--red);font-weight:700;font-size:22px}
.carryout{top:482px;left:963px;width:196px;height:36px;position:absolute;background:var(--red);border:2px solid var(--white);
  border-radius:18px;color:var(--black);font-family:"Roboto Condensed",sans-serif;font-size:24px;text-align:center;line-height:31px}
.hours-head{top:528px;font-style:italic;font-weight:700;color:var(--white);font-size:16px;font-family:"Roboto Condensed",sans-serif}
.hours-rule{position:absolute;left:1002px;top:550px;width:136px;height:1px;background:var(--white)}
.hours{position:absolute;left:932px;top:556px;font-family:"Roboto Condensed",sans-serif;font-size:16px;color:var(--white);line-height:20.5px}
.hours .d{font-style:italic;font-weight:700;display:inline-block}
.services{top:646px;color:var(--white);font-size:19px}
.services .star{color:var(--red);font-size:11px;vertical-align:2px}
.byob{top:668px;color:var(--white);font-style:italic;font-weight:700;font-size:15px}
.contact-band{position:absolute;left:918px;top:696px;width:306px;height:60px;background:var(--red);text-align:center;color:var(--white)}
.contact-band .addr{font-family:"Open Sans",sans-serif;font-size:14px;padding-top:5px;white-space:nowrap}
.contact-band .phone{font-family:"Open Sans",sans-serif;font-weight:700;font-size:25px;line-height:30px;display:flex;justify-content:center;align-items:center;gap:6px}
.web-band{position:absolute;left:918px;top:756px;width:306px;height:36px;background:var(--white);color:var(--black);
  text-align:center;font-size:16px;line-height:24px}
.map{position:absolute;left:625px;top:637px;width:278px;height:126px;background:var(--white)}
.caption{position:absolute;color:var(--white);font-size:9.5px;text-align:center}
</style>
</head>
<body>
<div class="sheet">

  <div class="block" style="left:12px;top:10px;width:280px">
    <div class="script-title left">Diet Steamer</div>
  </div>
  <div class="block" style="left:12px;top:40px;width:280px">
    <div class="row"><span class="item" style="font-weight:400;line-height:11px">Served with Jasmine or Brown Steamed Rice &amp; Gluten<br>Free Garlic Sauce</span><span class="price">$8.95</span></div>
  </div>
  <div class="block" style="left:12px;top:66px;width:200px">
    <div class="item">Steamed Mix Vegetable</div>
    <div class="note">Bean Sprout, Bok Choy, Broccoli, Carrot, Mushroom, Peapod</div>
    <div class="opt" style="grid-template-columns:86px 80px 1fr;margin-left:98px;line-height:14.6px;margin-top:2px;font-weight:700">
      <span>Vegetable</span><span style="font-weight:400">$8.95</span><span></span>
      <span>Chicken</span><span style="font-weight:400">$10.95</span><span></span>
      <span>Shrimp</span><span style="font-weight:400">$12.95</span><span></span>
    </div>
  </div>
  <div class="block" style="left:12px;top:133px;width:200px">
    <div class="item">Steamed Broccoli</div>
    <div class="note">Broccoli, Carrot</div>
    <div class="opt" style="grid-template-columns:86px 80px 1fr;margin-left:98px;line-height:14.6px;margin-top:2px;font-weight:700">
      <span>Vegetable</span><span style="font-weight:400">$8.95</span><span></span>
      <span>Chicken</span><span style="font-weight:400">$10.95</span><span></span>
      <span>Shrimp</span><span style="font-weight:400">$12.95</span><span></span>
    </div>
  </div>
  <div class="block" style="left:12px;top:194px;width:280px">
    <div class="row"><span class="item">Steamed Garden Green</span><span class="price">$8.95</span></div>
    <div class="note">Broccoli, Peapod, String Bean</div>
  </div>

  <div class="block" style="left:12px;top:226px;width:280px">
    <div class="row" style="align-items:center"><span class="script-title left" style="font-size:20px;width:170px">Beverage</span><span style="font-family:'Roboto Condensed',sans-serif;font-weight:700;font-size:20px;color:var(--white)">$3.95</span></div>
  </div>
  <div class="block" style="left:12px;top:258px;width:280px">
    <div class="row"><span class="item">Bubble Tea</span><span class="price">$1.95</span></div>
    <div class="note">Frozen Taiwanese Smoothie with Tapioca Pearl</div>
    <div class="opt" style="grid-template-columns:74px 58px 1fr;margin-left:16px;line-height:18px;margin-top:3px">
      <span>• Banana</span><span>• Coconut</span><span>• Strawberry</span>
      <span>• Milk Tea</span><span>• Pineapple</span><span></span>
    </div>
  </div>
  <div class="block" style="left:12px;top:316px;width:280px;line-height:14.2px">
    <div class="row"><span class="item">Meadowbrook Organic Chocolate Milk</span><span class="price">$1.95</span></div>
    <div class="row"><span class="item">Orange Juice</span><span class="price">$2.25</span></div>
    <div class="row"><span class="item">Japanese Soda</span><span class="price">$2.95</span></div>
    <div class="row"><span class="item">Thai Ice Tea</span><span class="price">$2.25</span></div>
    <div class="note" style="line-height:7px;margin-bottom:4px">Ceylon Taste Tea with Milk and Creamer</div>
    <div class="row"><span class="item">Alpine Sparkling Water</span><span class="price">$2.25</span></div>
  </div>
  <div class="block" style="left:12px;top:403px;width:118px">
    <div class="item">Bottled Ice Tea</div>
    <div class="opt" style="grid-template-columns:64px 1fr;margin-left:4px;line-height:13px"><span>• Unsweetened</span><span>•Raspberry</span></div>
    <div class="opt" style="grid-template-columns:56px 28px 1fr;margin-top:5px;line-height:14px">
      <span class="item">Soft Drink</span><span class="item">Bottle</span><span class="price">$2.25</span>
      <span></span><span class="item">2L</span><span class="price">$3.50</span>
    </div>
    <div class="opt" style="grid-template-columns:28px 42px 1fr;margin-left:4px;margin-top:6px;font-size:6.6px"><span>•Cola</span><span>• Diet Cola</span><span>• Lemon Soda</span></div>
  </div>
  <div class="photo" role="img" aria-label="Photo of a strawberry bubble tea in a glass mug" style="left:132px;top:412px;width:78px;height:118px;background:linear-gradient(180deg,#efe6dc,#e98f8a 45%,#b7a79a)"></div>
  <div class="photo" role="img" aria-label="Photo of a milk tea bubble tea in a glass mug" style="left:212px;top:412px;width:53px;height:118px;background:linear-gradient(180deg,#6a5448,#c9a384 50%,#7b6a5e)"></div>

  <div class="block" style="left:12px;top:543px;width:280px"><div class="script-title">Desert</div></div>
  <div class="block" style="left:12px;top:571px;width:280px">
    <div class="row"><span class="item">Fried Ice Cream</span><span class="price">$6.95</span></div>
    <div class="note">Deep Fried Scoop of Vanilla Ice Cream with Chocolate Syrup.</div>
    <div class="row" style="margin-top:7px"><span class="item">Banana Egg Roll</span><span class="price">$3.95</span></div>
    <div class="note" style="line-height:7px">Coconut Sugar Dusted Banana. Deep Fried in Egg Roll Wrapper with Carmel<br>Syrup. Add 1 Scoop of Vanilla Ice Cream (+$1)</div>
    <div class="row" style="margin-top:5px"><span class="item">Coconut Panna Cotta with Mango</span><span class="price">$3.95</span></div>
    <div class="note">Creamy Coconut Panna Cotta Topped with Mango Gel</div>
    <div class="row" style="margin-top:6px"><span class="item">Mochi Ice Cream (2)</span><span class="price">$4.50</span></div>
    <div class="note">Pounded Sticky Rice in Ice Cream Filling. Choice of Green Tea or Red Bean.</div>
    <div class="row" style="margin-top:6px"><span class="item">Sugar Dusted Biscuit</span><span class="price">$3.95</span></div>
    <div class="note">Golden Brown Biscuit Fully Covered with Sugar</div>
  </div>

  <div class="block" style="left:320px;top:10px;width:278px"><div class="script-title">Lunch Menu</div></div>
  <div class="block" style="left:320px;top:41px;width:278px;text-align:center;font-size:7px;line-height:11px;color:var(--white)">Lunch included 1 Entrée from either Classic or Jade Choice,<br>1 Side and 1 Starch</div>
  <div class="block" style="left:322px;top:73px;width:276px">
    <div class="section-head">Entrée</div>
    <div class="row" style="margin-top:3px"><span class="item">Classic Entrées</span><span class="price">$7.50</span></div>
    <div class="note">Ingredient Choices - Vegetable/Chicken/Beef or Shrimp(+$1)</div>
    <div class="opt" style="grid-template-columns:105px 1fr;margin-left:16px;line-height:17px;margin-top:3px;font-weight:600">
      <span>Kung Pao</span><span>Mix Vegetable</span>
      <span>Mongolian</span><span>Egg Foo Young (2 Patties)</span>
      <span>Szechwan</span><span>Lo Mein</span>
      <span>Broccoli</span><span>Fried Rice</span>
    </div>
  </div>
  <div class="block" style="left:320px;top:185px;width:278px">
    <div class="section-head">JADE Choice Entrées</div>
    <div style="line-height:14.3px;margin-top:4px">
      <div class="row"><span class="item">General Tso Chicken</span><span class="price">$7.50</span></div>
      <div class="row"><span class="item">Orange Chicken</span><span class="price">$7.50</span></div>
      <div class="row"><span class="item">Sesame Chicken</span><span class="price">$7.50</span></div>
      <div class="row"><span class="item">Sweet Sour Chicken</span><span class="price">$7.25</span></div>
      <div class="row"><span class="item">Thai Basil Chicken</span><span class="price">$7.95</span></div>
      <div class="row"><span class="item">Thai Basil Shrimp</span><span class="price">$8.95</span></div>
      <div class="row"><span class="item">Pepper Steak</span><span class="price">$7.50</span></div>
      <div class="row"><span class="item">Chili Pepper Beef</span><span class="price">$8.50</span></div>
      <div class="row"><span class="item">Bulgogi Beef</span><span class="price">$8.50</span></div>
      <div class="row"><span class="item">Honey Walnut Shrimp</span><span class="price">$9.50</span></div>
      <div class="row"><span class="item">Black Bean Flounder</span><span class="price">$8.95</span></div>
      <div class="row"><span class="item">Home Style Flounder</span><span class="price">$8.95</span></div>
      <div class="row"><span class="item">Tofu Home Style</span><span class="price">$7.50</span></div>
    </div>
  </div>
  <div class="block" style="left:346px;top:403px;width:92px;border-bottom:1px solid var(--white)"><div class="section-head">Side</div></div>
  <div class="block" style="left:466px;top:403px;width:132px;border-bottom:1px solid var(--white)"><div class="section-head">Starch</div></div>
  <ul class="bullets block" style="left:350px;top:422px">
    <li>Egg Roll (1)</li><li>Thai Beef Roll (1)</li><li>Crab Rangoon (1)</li><li>Egg Drop Soup</li><li>Hot &amp; Sour Soup</li><li>Wonton Soup</li>
  </ul>
  <ul class="bullets block" style="left:472px;top:422px">
    <li>White</li><li>Steamed Brown Rice</li><li>Egg Fried Rice</li>
  </ul>

  <div class="block" style="left:320px;top:533px;width:278px"><div class="script-title">Kids Menu</div></div>
  <div class="block" style="left:320px;top:569px;width:278px">
    <div class="row"><span class="item">Sweet Sour Chicken</span><span class="price">$4.95</span></div>
    <div class="note">White Meat Chicken with Sweet Sour Sauce</div>
    <div class="row" style="margin-top:7px"><span class="item">Chicken Lo Mein</span><span class="price">$4.95</span></div>
    <div class="note">White Meat Chicken and Lo Mein Noodle</div>
    <div class="row" style="margin-top:7px"><span class="item">Chicken Fried Rice</span><span class="price">$4.95</span></div>
    <div class="note">White Meat Chicken and Egg Fried Rice</div>
    <div class="row" style="margin-top:7px"><span class="item" style="display:flex;align-items:center;gap:3px">Tofu Broccoli Steamer
      <svg width="9" height="9" viewBox="0 0 10 10"><circle cx="5" cy="5" r="4.5" fill="#4a2a1c" stroke="#c9a36a"/></svg>
      <svg width="9" height="9" viewBox="0 0 10 10"><circle cx="5" cy="5" r="4.5" fill="#3a7a2a" stroke="#9fd27a"/></svg></span><span class="price">$4.95</span></div>
    <div class="note">Broccoli, Carrot &amp; Tofu w. White Sauce</div>
  </div>

  <div class="legend">
    <div style="display:grid;grid-template-columns:298px 1fr;row-gap:8px">
      <div class="key"><span class="dot" style="border:2px solid #8a5a3c;background:#2a1a12"></span>GF - Gluten Free</div>
      <div class="key"><span class="dot" style="border:2px solid #c9a13a;background:#2a2410"></span>NUT - Contain Nuts Product (Do Not Included Sesame Seeds)</div>
      <div class="key"><span class="dot" style="border:2px solid #6aa84f;background:#17300f"></span>VG - Vegetarian. May Contain Daily Product</div>
      <div class="key"><span class="dot" style="border:2px solid var(--red);background:#3a0a0c"></span>SP - Spicy</div>
    </div>
    <div style="margin-top:6px;line-height:12px;font-weight:600">We use Peanut, Shellfish, Fish, Milk, soy and Milk in our Kitchen. Please inform us piror your order if food allergy is a corcern.<br>We do our best to accommodate your needs. Your satisfiction is our priority.</div>
  </div>

  <div class="block" style="left:627px;top:12px;width:278px">
    <div class="row"><span style="font-style:italic;font-weight:700;font-size:13px;color:var(--white)">JADE Dinner for 2</span><span style="font-weight:700;font-size:14px;color:var(--white)">$29.95</span></div>
    <div style="font-size:5.6px;color:var(--white);margin-top:2px">Dinner for 2 included a Bowl of Soup, Starter, 2 Main Courses and Rice.</div>
  </div>
  <div class="pill">Complete Your Dinner with<br>Our Selected Desert &nbsp;for $3.</div>
  <div class="block" style="left:627px;top:103px;width:280px">
    <div class="section-head">Bowl of Soup (One)</div>
    <div class="opt" style="grid-template-columns:88px 1fr;margin-left:48px;font-size:6.8px"><span>• Egg Drop</span><span>• Hot &amp; Sour</span></div>
    <div class="section-head" style="margin-top:5px">Starters (One)</div>
    <div class="opt" style="grid-template-columns:118px 1fr;margin-left:34px;font-size:6.8px;line-height:14px;margin-top:2px">
      <span>• Chicken Lettuces Wrap</span><span>• Pan Fried Potsticker</span>
      <span>• Teriyaki Chicken Skewer</span><span>• Slow Braised Spare Rib</span>
    </div>
    <div class="section-head" style="margin-top:5px">Main Course (Two)</div>
    <div class="opt" style="grid-template-columns:104px 101px 1fr;margin-left:5px;font-size:6.8px;line-height:12.2px;margin-top:1px">
      <span>• General Tso Chicken</span><span>• Sesame Chicken</span><span>• Orange Chicken</span>
      <span>• Kung Pao Chicken</span><span>• Szechwan Chicken</span><span>• Chicken Lo Mein</span>
      <span>• Broccoli Beef</span><span>• Mongolian Beef</span><span>• Tofu Homestyle</span>
      <span>• Sweet &amp; Sour Chicken</span><span></span><span></span>
      <span>• Pepper Steak</span><span></span><span></span>
      <span>• Dry Fried String Bean</span><span></span><span></span>
    </div>
    <div class="section-head" style="margin-top:3px">Rice</div>
    <div style="font-size:6.8px;color:var(--white);line-height:11px">Choice of Jasmine White or Whole Grain Brown Rice.<br>Upgrade to Chicken Fried Rice(+$4)</div>
    <div class="section-head" style="margin-top:3px">Add a Desert (+$3)</div>
    <ul class="bullets" style="margin-left:14px;line-height:13px">
      <li>Banana Egg Roll</li><li>Coconut Panna Cotta with Mango</li><li>Sugar Dusted Biscuit</li><li>Mochi Ice Cream (2)</li>
    </ul>
  </div>
  <div class="notice"><b>Notice:</b><span>Tax and gratuity are not included. Not valid with any other offers or discounts. No Substitution.</span></div>
  <div class="caption" style="left:612px;top:459px;width:306px">BUSINESS STATEMENT</div>
  <div class="caption" style="left:612px;top:622px;width:306px">MINI MAP</div>
  <div class="map" role="img" aria-label="Simple sketch map showing the restaurant location near the main street intersection"></div>

  <div class="brand"><span class="name">LANTERN JADE</span><span class="mark"></span></div>
  <div class="front-photos" role="img" aria-label="Collage of six dish photos: stir-fried beef, spicy chicken, soup with crisp noodles, seafood with vegetables, lettuce wrap and rice noodles">
    <span style="background:linear-gradient(135deg,#e8e2da,#5a3424 60%,#3a2a20)"></span>
    <span style="background:linear-gradient(135deg,#f2eee8,#8a4a2a 60%,#5a3a24)"></span>
    <span style="background:linear-gradient(135deg,#f4f0ea,#9a3a22 55%,#e8c45a)"></span>
    <span style="background:linear-gradient(135deg,#3a3430,#6a8a3a 55%,#d9c8a8)"></span>
    <span style="background:linear-gradient(135deg,#cfe0b8,#6a4a30 60%,#efeae2)"></span>
    <span style="background:linear-gradient(135deg,#f4f2ee,#e4e0d6 60%,#6a8a3a)"></span>
  </div>
  <div class="front-text tagline">Casual Chinese Restaurant</div>
  <div class="carryout">Carry Out Menu</div>
  <div class="front-text hours-head">Open Hours</div>
  <div class="hours-rule"></div>
  <div class="hours">
    <div><span class="d" style="width:145px">Tuesday to Thursday</span>11:00am - 9:00pm</div>
    <div><span class="d" style="width:145px">Friday and Saturday</span>11:00am - 9:30pm</div>
    <div><span class="d" style="width:145px;padding-left:78px">Sunday</span>12:00noon - 9:00pm</div>
    <div style="padding-left:76px"><span class="d">Closed On Monday</span></div>
  </div>
  <div class="front-text services">Dine In<span class="star">★</span> Carry Out<span class="star">★</span> Delivery<span class="star">★</span> Catering</div>
  <div class="front-text byob">B.Y.O.B. Welcome</div>
  <div class="contact-band">
    <div class="addr">2871 W Orchard Ave, St Charles IL 60178</div>
    <div class="phone"><svg width="22" height="22" viewBox="0 0 24 24"><path fill="#000" d="M6.6 10.8a15.1 15.1 0 0 0 6.6 6.6l2.2-2.2a1 1 0 0 1 1-.25 11.4 11.4 0 0 0 3.6.57 1 1 0 0 1 1 1V20a1 1 0 0 1-1 1A17 17 0 0 1 3 4a1 1 0 0 1 1-1h3.5a1 1 0 0 1 1 1c0 1.25.2 2.45.57 3.57a1 1 0 0 1-.25 1z"/></svg>630-412-8836</div>
  </div>
  <div class="web-band">www.LanternJade.example</div>
</div>
</body>
</html>
```